Brindlecove (main name) sharpening systems(underneath)

Specializing in Knife, Scissors and Clipper sharpening, repair and maintenance.
I would like a logo designed that has at least one of the elements above showing what could happen as a result of the instrument being sharpened by my company as part of the logo (maybe the word Brindlecove being cut in half)

Target Market(s)

commercial (restaurants or any establishment that deals with food preparation, salons, barbershops) residential (any homes that use knives scissors or clippers)

Contact Information for Business Card

Name: Marcus Pellingham
Address: K240 Coral Vista Heights
Cell: 12465917362
Email: brindlecovehone@mailtrove.net

Requirements
Must have
• Brindlecove....sharpening systems clean front with strong logo indicating what we do as part of logo front of card
• Contact details: back of card
• we sharpen on site or pick up and drop off within 24hrs (at back of Card)
• telephone number: (at back) for contact
• address and other details (at back)

```html
<!DOCTYPE html>
<html lang="en">
<head>
<meta charset="utf-8">
<title>Brindlecove Business Card</title>
<link href="https://fonts.googleapis.com/css2?family=Montserrat:wght@400;500;600;800&display=swap" rel="stylesheet">
<style>
  :root {
    --backdrop: #2b2b2d;
    --card: #050505;
    --ink: #ffffff;
    --accent: #3ab4e6;
    --muted: #e6e6e6;
  }
  * { margin: 0; padding: 0; box-sizing: border-box; }
  html, body {
    width: 1200px; height: 900px; overflow: hidden;
    background: var(--backdrop);
    font-family: "Montserrat", Arial, sans-serif;
  }
  .canvas { position: relative; width: 1200px; height: 900px; }
  .card {
    position: absolute;
    width: 580px; height: 332px;
    background: var(--card);
    border-radius: 22px;
    overflow: hidden;
    box-shadow: 0 18px 40px rgba(0,0,0,0.45);
  }
  .card--front { left: 90px; top: 80px; }
  .card--back { left: 530px; top: 488px; }

  .brand { position: absolute; }
  .wordmark {
    display: flex; align-items: center; gap: 10px;
    font-weight: 800;
    letter-spacing: 1px;
    color: var(--ink);
    line-height: 1;
    white-space: nowrap;
  }
  .wordmark__mark { background: var(--accent); flex: none; }
  .tagline {
    font-weight: 600;
    letter-spacing: 4px;
    color: var(--accent);
    text-transform: uppercase;
    white-space: nowrap;
  }

  .card--front .brand { left: 44px; top: 140px; }
  .card--front .wordmark { font-size: 40px; }
  .card--front .wordmark__mark { width: 14px; height: 14px; }
  .card--front .tagline { font-size: 13px; margin: 10px 0 0 24px; }

  .card--back .brand { right: 30px; top: 196px; text-align: right; }
  .card--back .wordmark { font-size: 28px; gap: 8px; }
  .card--back .wordmark__mark { width: 10px; height: 10px; }
  .card--back .tagline { font-size: 9.5px; letter-spacing: 3px; margin-top: 7px; }

  .site-url {
    position: absolute; right: 30px; bottom: 26px;
    font-size: 15px; font-weight: 500; color: var(--ink);
    letter-spacing: 0.3px;
  }
  .site-url__name { color: var(--accent); }

  .service-note {
    position: absolute; left: 44px; top: 34px;
    font-size: 12px; font-weight: 500; color: var(--muted);
    line-height: 18px;
  }
  .service-note strong { color: var(--accent); font-weight: 600; }

  .side-tab {
    position: absolute; left: 0; top: 182px;
    width: 22px; height: 126px;
    background: var(--accent);
    border-radius: 0 0 14px 0;
  }
  .contact { position: absolute; left: 44px; top: 140px; color: var(--muted); }
  .contact__name {
    font-size: 21px; font-weight: 600; color: var(--accent);
    letter-spacing: 0.5px; margin-bottom: 2px;
  }
  .contact__role { font-size: 12px; margin-bottom: 6px; }
  .contact__line { font-size: 12px; line-height: 17px; }
  .contact__line--last { margin-bottom: 4px; }
  .contact__row {
    display: flex; align-items: center; gap: 9px;
    font-size: 12px; line-height: 19px;
  }
  .contact__row svg { width: 10px; height: 10px; flex: none; }
  .icon-fill { fill: var(--accent); }
  .icon-line { fill: none; stroke: var(--accent); stroke-width: 1; }
  .accent { color: var(--accent); }
</style>
</head>
<body>
<main class="canvas">
  <section class="card card--front" aria-label="Card front">
    <div class="brand">
      <div class="wordmark"><span class="wordmark__mark"></span>BRINDLECOVE</div>
      <p class="tagline">Sharpening Systems</p>
    </div>
    <p class="site-url">www.<span class="site-url__name">brindlecove</span>.net</p>
  </section>

  <section class="card card--back" aria-label="Card back">
    <p class="service-note">We sharpen <strong>on site</strong> or <strong>pick up &amp; drop off within 24 hrs</strong></p>
    <div class="side-tab"></div>
    <div class="contact">
      <p class="contact__name">Marcus Pellingham</p>
      <p class="contact__role">Director</p>
      <p class="contact__line">K240 Coral Vista Heights</p>
      <p class="contact__line contact__line--last">Harbour Row Unit 7</p>
      <p class="contact__row">
        <svg viewBox="0 0 10 10"><path class="icon-fill" d="M2 0.5 L3.8 2.6 L2.9 3.8 Q4 6 6.2 7.1 L7.4 6.2 L9.5 8 L8.4 9.5 Q4 9 0.5 1.6 Z"/></svg>
        +1-246-591-7362
      </p>
      <p class="contact__row">
        <svg viewBox="0 0 10 10"><path class="icon-line" d="M0.5 2 H9.5 V8 H0.5 Z M1.2 2.6 L5 5.4 L8.8 2.6"/></svg>
        brindlecovehone@mailtrove.net
      </p>
      <p class="contact__row">
        <svg viewBox="0 0 10 10"><circle class="icon-fill" cx="5" cy="5" r="4.5"/></svg>
        <span>www.<span class="accent">brindlecove</span>.net</span>
      </p>
    </div>
    <div class="brand">
      <div class="wordmark"><span class="wordmark__mark"></span>BRINDLECOVE</div>
      <p class="tagline">Sharpening Systems</p>
    </div>
  </section>
</main>
</body>
</html>
```